Brantley Water Taxi and Transport

Need to redesign our business cards to relay that we do freight logistics and water taxi service. We also work with gov. agencies doing environmental clean up, oil spill response, remote site construction and work with many of the air taxi and helicopter services on Kodiak Island. Out website is www.brantleywatertaxi-example.com to get a better idea of what we do.

Contact Information for Business Card

I have a previous business card but it just has the logo on the front, and a sunset picture on the back with the contact info. It does not relay what we do and what we can help with. I like a simple straight forward design over a busy one.

Colors
3176b5
0455a3
cfdfed

Requirements
Must have
• logo, email, website, phone number

```html
<!DOCTYPE html>
<html lang="en">
<head>
<meta charset="utf-8">
<title>Brantley Water Taxi and Transport – Business Card</title>
<link href="https://fonts.googleapis.com/css2?family=Questrial&family=Roboto:wght@500;700&display=swap" rel="stylesheet">
<style>
  :root {
    --blue-deep: #0455a3;
    --blue-mid: #3176b5;
    --blue-pale: #cfdfed;
    --white: #ffffff;
    --page: #ffffff;
  }
  * { box-sizing: border-box; margin: 0; padding: 0; }
  html, body { width: 1200px; height: 1200px; overflow: hidden; background: var(--page); }
  .canvas { position: relative; width: 1200px; height: 1200px; }

  .card { position: absolute; left: 180px; width: 840px; height: 480px; overflow: hidden; }
  .card--front { top: 70px; background: var(--blue-deep); }
  .card--back { top: 600px; background: var(--blue-pale); }
  .card__shape { position: absolute; inset: 0; }

  .brand { font-family: "Questrial", sans-serif; font-weight: 400; text-align: center; line-height: 1; }
  .brand__name { display: block; letter-spacing: 1px; }
  .brand__tagline { display: block; }

  .front-badge {
    position: absolute; left: 286px; top: 58px; width: 268px; height: 268px;
    border-radius: 50%; background: var(--blue-pale);
    display: flex; align-items: center; justify-content: center;
  }
  .front-badge .brand { color: var(--blue-deep); margin-top: 70px; }
  .front-badge .brand__name { font-size: 44px; }
  .front-badge .brand__tagline { font-size: 17px; margin-top: 6px; }

  .front-url {
    position: absolute; left: 0; right: 0; top: 420px;
    font-family: "Roboto", sans-serif; font-weight: 700; font-size: 32px;
    color: var(--blue-deep); text-align: center;
  }

  .back-brand { position: absolute; left: 72px; width: 268px; top: 262px; color: var(--blue-deep); }
  .back-brand .brand__name { font-size: 60px; }
  .back-brand .brand__tagline { font-size: 24px; margin-top: 10px; }

  .back-title { position: absolute; left: 520px; width: 300px; top: 34px; color: var(--blue-pale); text-align: left; }
  .back-title .brand__name { font-size: 56px; }
  .back-title .brand__tagline { font-size: 24px; margin-top: 10px; }

  .contact-list { position: absolute; left: 475px; top: 172px; list-style: none; }
  .contact-item { display: flex; align-items: center; height: 34px; margin-bottom: 40px; }
  .contact-item:nth-child(2) { margin-bottom: 42px; }
  .contact-icon {
    width: 34px; height: 34px; border-radius: 50%; background: var(--blue-pale);
    display: flex; align-items: center; justify-content: center; margin-right: 11px; flex: none;
  }
  .contact-icon svg { width: 20px; height: 20px; }
  .contact-text { font-family: "Roboto", sans-serif; font-weight: 500; font-size: 18px; color: var(--white); }
</style>
</head>
<body>
<main class="canvas">

  <section class="card card--front" aria-label="Card front">
    <svg class="card__shape" viewBox="0 0 840 480" aria-hidden="true">
      <path fill="var(--blue-pale)" d="M0,410 Q12,394 50,398 Q80,404 98,412 Q132,424 148,410 Q170,394 198,398 Q228,404 248,412 Q280,424 297,410 Q320,394 348,398 Q378,404 396,412 Q430,424 446,410 Q468,394 496,398 Q526,404 545,412 Q578,424 595,410 Q618,394 646,398 Q676,404 694,412 Q728,424 744,410 Q766,394 794,398 Q824,404 840,410 L840,480 L0,480 Z"/>
    </svg>
    <div class="front-badge">
      <p class="brand">
        <span class="brand__name">BRANTLEY</span>
        <span class="brand__tagline">Water Taxi &amp; Transport</span>
      </p>
    </div>
    <p class="front-url">www.brantleywatertaxi-example.com</p>
  </section>

  <section class="card card--back" aria-label="Card back">
    <svg class="card__shape" viewBox="0 0 840 480" aria-hidden="true">
      <path fill="var(--blue-deep)" d="M420,0 Q420,48 440,52 Q452,60 452,80 Q452,100 440,106 Q420,112 420,132 Q420,152 440,158 Q452,164 452,184 Q452,204 440,210 Q420,216 420,236 Q420,256 440,262 Q452,268 452,288 Q452,308 440,314 Q420,320 420,340 Q420,360 440,366 Q452,372 452,392 Q452,412 440,418 Q420,424 420,444 Q420,470 440,480 L840,480 L840,0 Z"/>
    </svg>

    <p class="brand back-brand">
      <span class="brand__name">BRANTLEY</span>
      <span class="brand__tagline">Water Taxi &amp; Transport</span>
    </p>

    <p class="brand back-title">
      <span class="brand__name">BRANTLEY</span>
      <span class="brand__tagline">Water Taxi &amp; Transport</span>
    </p>

    <ul class="contact-list">
      <li class="contact-item">
        <span class="contact-icon">
          <svg viewBox="0 0 24 24" aria-hidden="true"><path fill="var(--blue-deep)" d="M6.6 10.8a15.1 15.1 0 0 0 6.6 6.6l2.2-2.2c.3-.3.7-.4 1-.2 1.1.4 2.3.6 3.6.6.6 0 1 .4 1 1V20c0 .6-.4 1-1 1A17 17 0 0 1 3 4c0-.6.4-1 1-1h3.5c.6 0 1 .4 1 1 0 1.3.2 2.5.6 3.6.1.3 0 .7-.2 1z"/></svg>
        </span>
        <span class="contact-text">555-014-3400</span>
      </li>
      <li class="contact-item">
        <span class="contact-icon">
          <svg viewBox="0 0 24 24" aria-hidden="true" fill="none" stroke="var(--blue-deep)" stroke-width="2"><circle cx="12" cy="12" r="9"/><ellipse cx="12" cy="12" rx="4" ry="9"/><path d="M3 12h18M5 7h14M5 17h14"/></svg>
        </span>
        <span class="contact-text">http://www.brantleywatertaxi-example.com</span>
      </li>
      <li class="contact-item">
        <span class="contact-icon">
          <svg viewBox="0 0 24 24" aria-hidden="true" fill="none" stroke="var(--blue-deep)" stroke-width="2"><rect x="3" y="6" width="18" height="12" rx="1"/><path d="M3 6l9 7 9-7M3 18l7-6M21 18l-7-6"/></svg>
        </span>
        <span class="contact-text">brantleywatertaxi@example.com</span>
      </li>
    </ul>
  </section>

</main>
</body>
</html>
```